Flyer-Design für Mittagsbelieferung
Zielgruppe
Mittags Belieferung ältere Menschen, Firmen, Berufstätige
Aufgabenstellung
Text aus Datei den Bestellzettel nicht weiter beachten nur Seite 2 u.3... Logo vielleicht vorne drauf... Format bin ich unentschieden

```html
<!DOCTYPE html>
<html lang="de">
<head>
<meta charset="utf-8">
<title>pilvo – Flyer Mittagsbelieferung</title>
<link href="https://fonts.googleapis.com/css2?family=Tillana:wght@400;600;700&display=swap" rel="stylesheet">
<style>
:root{
  --yellow:#f8c53f;
  --gold:#f9b700;
  --orange:#e8500e;
  --red:#d42a1c;
  --green:#98c11b;
  --cream:#fde2a3;
  --ink:#2b2b2b;
  --white:#ffffff;
  --stage:#d9d9d9;
}
*{box-sizing:border-box;margin:0;padding:0}
html,body{width:1200px;height:484px;overflow:hidden;background:var(--stage)}
body{font-family:"Tillana",sans-serif;color:var(--ink);position:relative}
.spread{position:absolute;top:10px;width:780px;height:827px;transform:scale(.56);transform-origin:0 0;overflow:hidden;background:var(--white)}
.spread--outside{left:143px}
.spread--inside{left:620px}
.abs{position:absolute}
.photo{position:absolute}

/* back panel */
.back{left:0;top:0;width:390px;height:827px;background:var(--yellow)}
.map{left:0;top:0;width:390px;height:130px;background:linear-gradient(160deg,#f1e6c4,#e9d9a6 60%,var(--yellow))}
.area-band{left:0;top:130px;width:390px;height:27px;background:var(--orange);color:var(--white);font-size:17px;font-weight:600;padding:2px 0 0 24px;white-space:nowrap}
.area-list{left:0;top:157px;width:390px;height:170px;background:var(--white);border-bottom:3px solid var(--orange);display:flex;gap:26px;padding:10px 0 0 24px;font-size:17px;line-height:23.5px;white-space:nowrap}
.area-list ul{list-style:none}
.brand-badge{left:23px;top:313px;width:120px;height:120px;border-radius:50%;background:var(--white);border:4px solid var(--orange);display:flex;align-items:center;justify-content:center;font-size:30px;font-weight:700;color:var(--orange)}
.address{left:175px;top:375px;width:215px;height:170px;background:var(--white);border-bottom:3px solid var(--orange);padding:14px 0 0 14px;font-size:15.5px;line-height:23px;white-space:nowrap}
.address .pin{position:absolute;right:18px;top:22px}
.scooter-photo{left:0;top:440px;width:390px;height:387px;background:radial-gradient(circle at 40% 45%,#d8332a 0,#c9272b 30%,transparent 60%),linear-gradient(180deg,var(--yellow),#f6d04a)}

/* front panel */
.front{left:390px;top:0;width:390px;height:827px}
.courier-photo{left:0;top:0;width:390px;height:573px;background:linear-gradient(135deg,#1d1f22 0,#2c2c2e 35%,#c9352a 60%,#e2412e 100%)}
.front-brand{left:22px;top:38px;display:flex;align-items:center;gap:10px;color:var(--white);font-size:34px;font-weight:700}
.front-brand .dot{width:30px;height:30px;border-radius:50%;background:var(--orange)}
.contact{left:0;top:467px;width:275px;height:78px;background:var(--white);padding:8px 0 0 20px;color:var(--orange);font-size:22px;line-height:31px;white-space:nowrap}
.contact svg{vertical-align:-2px;margin-right:6px}
.offer{left:0;top:573px;width:390px;height:169px;background:var(--gold);padding:12px 0 0 24px}
.offer h1{font-size:35px;font-weight:700;line-height:46px;color:#231f20;white-space:nowrap}
.offer .sub{font-size:21px;margin-top:6px;white-space:nowrap}
.offer .price-line{font-size:21px;margin-top:6px;display:flex;align-items:center;gap:8px}
.price-tag{background:var(--orange);color:var(--white);font-size:34px;font-weight:700;border-radius:24px;padding:0 16px;line-height:44px}
.hours{left:0;top:742px;width:390px;height:85px;background:var(--orange);color:var(--white);font-size:16.5px;line-height:24px;padding:13px 0 0 24px;white-space:nowrap}

/* inside left */
.food-photo{left:0;top:0;width:390px;height:827px;background:linear-gradient(170deg,#2f5e22 0,#3a2a1e 25%,#c9792c 45%,#a8561e 70%,#3a2a1e 100%)}
.menu-cta{left:0;top:457px;width:390px;height:148px;background:var(--green);color:var(--white);font-size:16px;line-height:23px;padding:14px 0 0 24px}
.menu-cta p{width:245px}
.menu-cta .mark{position:absolute;right:20px;top:24px;width:94px;height:94px;border-radius:50%;background:var(--white)}

/* inside right */
.details{left:390px;top:0;width:390px;height:827px;font-size:16.5px;line-height:23px}
.service-box{position:absolute;left:22px;top:22px;width:346px;height:200px;background:var(--cream);border:3px dotted var(--orange);padding:14px 14px;font-size:16px;line-height:23px}
.service-box .intro{width:310px}
.service-box svg{position:absolute;right:12px;top:100px}
.price-head{position:absolute;left:0;top:230px;width:390px;text-align:center;color:var(--red);font-size:23px;line-height:35px;font-weight:600}
.cake-photo{left:22px;top:313px;width:172px;height:117px;background:linear-gradient(135deg,#4a2c1a,#c88a3a 45%,#e8a33a 60%,#c8243a)}
.cake-text{position:absolute;left:202px;top:310px;width:170px}
.cake-text em{font-style:normal;color:var(--red)}
.payment{position:absolute;left:22px;top:450px;width:350px}
.payment b{font-weight:700}
.payment .gap{margin-top:23px}
.payment .highlight{color:var(--red);font-weight:700}
</style>
</head>
<body>

<section class="spread spread--outside" aria-label="Außenseite">
  <div class="abs back">
    <div class="photo map" role="img" aria-label="Landkarte des Liefergebiets"></div>
    <div class="abs area-band">Derzeitiges Auslieferungsgebiet:</div>
    <div class="abs area-list">
      <ul><li>Gägelow</li><li>Proseken</li><li>Barnekow</li><li>Zierow</li><li>Gressow</li><li>Stofferdorf</li></ul>
      <ul><li>Woltersdorf</li><li>Wismar</li><li>Neuburg</li><li>Hornstorf</li><li>Kritzow</li><li>Auch weitere möglich!</li></ul>
    </div>
    <div class="photo scooter-photo" role="img" aria-label="Lieferfahrer in roter Kleidung auf einem Motorroller mit Essensbox"></div>
    <div class="abs brand-badge">pilvo</div>
    <div class="abs address">
      <svg class="pin" width="22" height="32" viewBox="0 0 22 32"><path d="M11 0C5 0 0 5 0 11c0 8 11 21 11 21s11-13 11-21C22 5 17 0 11 0z" fill="#e8500e"/><circle cx="11" cy="11" r="4.5" fill="#fff"/></svg>
      pilvo-Restaurant<br>Lindenweg 7<br>23968 Gägelow<br><br>Tel.: 03841/5527306<br>E-Mail: pilvo@postfeld.de
    </div>
  </div>

  <div class="abs front">
    <div class="photo courier-photo" role="img" aria-label="Lächelnder Lieferfahrer in roter Weste öffnet eine Thermobox"></div>
    <div class="abs front-brand"><span class="dot"></span>pilvo</div>
    <div class="abs contact">
      <div><svg width="20" height="20" viewBox="0 0 24 24"><path d="M6.6 10.8a15 15 0 0 0 6.6 6.6l2.2-2.2a1 1 0 0 1 1-.25 11.4 11.4 0 0 0 3.6.6 1 1 0 0 1 1 1V20a1 1 0 0 1-1 1A17 17 0 0 1 3 4a1 1 0 0 1 1-1h3.5a1 1 0 0 1 1 1c0 1.25.2 2.45.6 3.6a1 1 0 0 1-.25 1z" fill="#e8500e"/></svg>03841/55 27 306</div>
      <div><svg width="20" height="20" viewBox="0 0 24 24"><path d="M2 11 22 2l-9 20-2-9z" fill="#e8500e"/></svg>pilvo@postfeld.de</div>
    </div>
    <div class="abs offer">
      <h1>Ihr Wunschmenü</h1>
      <div class="sub">inkl. Nachtisch und Lieferung</div>
      <div class="price-line">für nur <span class="price-tag">6,00€</span></div>
    </div>
    <div class="abs hours">Lieferung: Mo. – Sa. 10.30 – 12.30 Uhr<br>An-und Abbestellungen: bis 10.00 Uhr</div>
  </div>
</section>

<section class="spread spread--inside" aria-label="Innenseiten">
  <div class="photo food-photo" role="img" aria-label="Paniertes Schnitzel mit Tomaten, Rucola, Brot und Soße auf Holzbrett"></div>
  <div class="abs menu-cta">
    <p>Fordern Sie noch heute einen Speiseplan von uns an und lassen Sie sich von unseren täglich frisch zubereiteten Speisen überzeugen.</p>
    <span class="mark" aria-hidden="true"></span>
  </div>

  <div class="abs details">
    <div class="service-box">
      <p class="intro">Wir liefern gerne Ihr Wunschmenü in unseren Thermoboxen zu Ihnen nach Hause oder auch ins Büro oder zum Arbeitsplatz.</p>
      <p style="margin-top:23px">Sie haben täglich die Wahl<br>zwischen 3 Menüs inkl. Nachtisch.</p>
      <svg width="64" height="58" viewBox="0 0 70 64" fill="none" stroke="#2b2b2b" stroke-width="2.5"><rect x="4" y="20" width="36" height="40"/><path d="M4 20l6-12h24l6 12"/><path d="M40 46h16l10-6v14H40"/></svg>
    </div>
    <div class="price-head">Preis pro Menü inkl. Nachtisch<br>und Lieferung: 6,00 €</div>
    <div class="photo cake-photo" role="img" aria-label="Stücke von selbstgebackenem Kuchen mit Himbeeren"></div>
    <p class="cake-text">1 Stück selbstge­backenen Kuchen liefern wir Ihnen gerne für <em>1,50 €</em> mit dazu.</p>
    <div class="payment">
      <p><b>Bei der Bezahlung haben Sie die Wahl</b> zwischen Barzahlung und Monatsrech­nung.</p>
      <p class="gap"><b>Barzahlung:</b> immer Montags im Voraus beim Fahrer gegen Erhalt der Wochen­rechnung.</p>
      <p><b>Monatsrechnung:</b> am Ende des Monats wird Ihnen eine Rechnung für den jewei­ligen Monat ausgestellt die Sie dann einfach überweisen.</p>
      <p class="gap"><span class="highlight">Keine Vertragsbindung!</span><br>Sollte es Ihnen nicht gefallen können Sie jederzeit wieder abbestellen.</p>
    </div>
  </div>
</section>

</body>
</html>
```